I am looking for a design that represent my gym/ performance facility that says respect the process on it. This images will be a center piece wall for my gym. I want this wall to stand out. This wall has to be clean and professional. This wall has to be Black and white. The gym is for athletes and regular members so the message has to relate to all. Respect the process represents this wall. Please be creative but clean and professional. Feel free to play with black and white body art. The message again should be "Respect The Process"
THE WALL IS 16FT LONG

Target Market(s)

Fitness and Athletes

Font styles to use
Sans Serif

Requirements
Must have
• Respect The Process
• Must all be in Black and white even images if you use them.
• Motivation words or phrases I.e., "Determination, Focus, Discipline,
• Please use famous or legendary athletes quotes.
• words to use:
• Transformation, Power, success, Strength, Commitment, Motivation, No Excuses, No Regrets, Never Give UP, Beast, Results, Dream Big, Consistency, Hard Work, Challenge,Warrior, Sacrifice, Greatness, Legendary, Winning, Zone, Purpose, Fight, Destiny,
• This Quote will stand alone:
• I HATED EVERY MINUTE OF TRAINING,
• BUT I SAID, "DON'T QUIT.
• SUFFER NOW AND LIVE THE REST
• OF YOUR LIFE A CHAMPION."
• -TOBIAS KRELLEN
• "IF YOU DON'T WANT TO SACRIFICE FOR WHAT YOU WANT
• WHAT YOU WANT BECOMES THE SACRIFICE."
• "EVERYONE HAS THE DESIRE TO WIN, BUT ONLY CHAMPIONS HAVE THE DESIRE TO PREPARE."
• "IT'S ALWAYS SEEMS IMPOSSIBLE UNTIL IT'S DONE."
Nice to have
• It would be nice to have the words in Mustard yellow print as well as the white.T

```html
<!DOCTYPE html>
<html lang="en">
<head>
<meta charset="utf-8">
<title>Respect The Process – Wall Concepts</title>
<link rel="stylesheet" href="https://fonts.googleapis.com/css2?family=Jost:wght@400;500;700&display=swap">
<style>
  :root {
    --wall-black: #1e2120;
    --divider: #e6e6e6;
    --mustard: #f0b91c;
    --white: #ffffff;
  }
  html, body {
    margin: 0;
    padding: 0;
    width: 1200px;
    height: 948px;
    overflow: hidden;
    background: var(--divider);
  }
  .wall-concepts {
    width: 1200px;
    height: 948px;
    display: flex;
    flex-direction: column;
    justify-content: space-between;
  }
  .wall-panel {
    display: block;
    width: 1200px;
    height: 315px;
    background: var(--wall-black);
    font-family: 'Jost', sans-serif;
  }
  .wall-panel .quote { text-anchor: middle; font-weight: 400; }
  .wall-panel .quote--sm { font-size: 8.3px; }
  .wall-panel .quote--md { font-size: 9.6px; }
  .wall-panel .quote--lg { font-size: 12px; }
  .wall-panel .headline { font-weight: 700; font-size: 60px; text-anchor: middle; }

  .wall-panel--mustard-title .headline { fill: var(--mustard); }
  .wall-panel--mustard-title .quote { fill: var(--white); }

  .wall-panel--all-white .headline,
  .wall-panel--all-white .quote { fill: var(--white); }

  .wall-panel--all-mustard .headline,
  .wall-panel--all-mustard .quote { fill: var(--mustard); }
</style>
</head>
<body>
<main class="wall-concepts">

  <svg class="wall-panel wall-panel--mustard-title" viewBox="0 0 1200 315" role="img" aria-label="Respect The Process – mustard title version">
    <text class="quote quote--sm" x="587" y="54">“Nobody who ever gave his best regretted it.” – Harlan Brecke</text>
    <text class="quote quote--md" x="587" y="71">“Without self-discipline, success is impossible, period.” – Dale Wintrop</text>
    <text class="quote quote--lg" x="587" y="89">“When you’ve got something to prove, there’s nothing greater than a challenge.” – Corey Vandall</text>
    <text class="headline" x="591" y="175" textLength="665" lengthAdjust="spacing">RESPECT THE PROCESS</text>
    <text class="quote quote--lg" x="587" y="224">“Never say never because limits, like fears, are often just an illusion.” – Marcus Delane</text>
    <text class="quote quote--md" x="587" y="241">“The harder the battle, the sweeter the victory.” – Reid Ashby</text>
    <text class="quote quote--sm" x="587" y="257">“Make each day your masterpiece.” – Arthur Kellum</text>
  </svg>

  <svg class="wall-panel wall-panel--all-white" viewBox="0 0 1200 315" role="img" aria-label="Respect The Process – white version">
    <text class="quote quote--sm" x="587" y="54">“Nobody who ever gave his best regretted it.” – Harlan Brecke</text>
    <text class="quote quote--md" x="587" y="71">“Without self-discipline, success is impossible, period.” – Dale Wintrop</text>
    <text class="quote quote--lg" x="587" y="89">“When you’ve got something to prove, there’s nothing greater than a challenge.” – Corey Vandall</text>
    <text class="headline" x="591" y="175" textLength="665" lengthAdjust="spacing">RESPECT THE PROCESS</text>
    <text class="quote quote--lg" x="587" y="224">“Never say never because limits, like fears, are often just an illusion.” – Marcus Delane</text>
    <text class="quote quote--md" x="587" y="241">“The harder the battle, the sweeter the victory.” – Reid Ashby</text>
    <text class="quote quote--sm" x="587" y="257">“Make each day your masterpiece.” – Arthur Kellum</text>
  </svg>

  <svg class="wall-panel wall-panel--all-mustard" viewBox="0 0 1200 315" role="img" aria-label="Respect The Process – mustard version">
    <text class="quote quote--sm" x="587" y="54">“Nobody who ever gave his best regretted it.” – Harlan Brecke</text>
    <text class="quote quote--md" x="587" y="71">“Without self-discipline, success is impossible, period.” – Dale Wintrop</text>
    <text class="quote quote--lg" x="587" y="89">“When you’ve got something to prove, there’s nothing greater than a challenge.” – Corey Vandall</text>
    <text class="headline" x="591" y="175" textLength="665" lengthAdjust="spacing">RESPECT THE PROCESS</text>
    <text class="quote quote--lg" x="587" y="224">“Never say never because limits, like fears, are often just an illusion.” – Marcus Delane</text>
    <text class="quote quote--md" x="587" y="241">“The harder the battle, the sweeter the victory.” – Reid Ashby</text>
    <text class="quote quote--sm" x="587" y="257">“Make each day your masterpiece.” – Arthur Kellum</text>
  </svg>

</main>
</body>
</html>
```